High-end construction company needs a business card design

We need a modern looking business card that draws people in, is memorable and looks so good people will want to sick it on their fridges.
On the first side what is needed are:
Logo
My name - Tomas Verbelk
Title - Managing Director
Website - www.kravel.co.uk
Email - tomas@kravel.co.uk
Telephone - 020 5194 6381
Mobile - 07845319027
On the back side was is needed is a list of all the services we provide:
-Kitchen Renovations
-Bathroom Renovations
-House Renovations
-Garage Conversions
-Extensions
-Loft Conversions
-Conservatories
-Carpentry
-Tiling
-Electrical
-Plumbing & Heating
-Bricklaying
-Landscaping
-Decorating
-Plastering
We would like the colours to be the same shades as on the logo with grey or black for the words.
Target Market(s)
Anyone who needs building work done
Contact Information for Business Card
This business card is for a construction company which strives to deliver excellent service and quality.
The look and feel of the card should represent this.
Requirements
Must have
- On the first side what is needed are:
Logo
My name - Tomas Verbelk
Title - Managing Director
Website - www.kravel.co.uk
Email - tomas@kravel.co.uk
Telephone - 020 5194 6381
Mobile - 07845319027
Nice to have
- Cool looking features

```html
<!DOCTYPE html>
<html lang="en">
<head>
<meta charset="utf-8">
<title>Kravel Construction Ltd – Business Card</title>
<link rel="stylesheet" href="https://fonts.googleapis.com/css2?family=Montserrat:wght@500;700&family=Open+Sans:wght@400;600&display=swap">
<style>
  :root {
    --backdrop: #4a4a4a;
    --card: #ffffff;
    --green: #7cc24a;
    --green-band: #78c045;
    --green-dark: #4b9438;
    --green-text: #6ab04c;
    --ink: #1f1f1f;
    --radius: 34px;
  }
  * { margin: 0; padding: 0; box-sizing: border-box; }
  html, body { width: 1200px; height: 982px; overflow: hidden; }
  body {
    background: var(--backdrop);
    position: relative;
    font-family: "Open Sans", Arial, sans-serif;
  }
  .card {
    position: absolute;
    left: 303px;
    width: 622px;
    height: 357px;
    background: var(--card);
    border-radius: var(--radius);
    overflow: hidden;
    box-shadow: 0 8px 18px rgba(0,0,0,0.35);
  }
  .card--services { top: 113px; }
  .card--contact { top: 513px; }

  .wordmark {
    position: absolute;
    font-family: "Montserrat", Arial, sans-serif;
    font-weight: 700;
    color: var(--green);
    text-align: center;
    line-height: 1;
  }
  .wordmark__name { display: block; font-size: 52px; letter-spacing: 1px; }
  .wordmark__sub { display: block; font-size: 14.5px; letter-spacing: 2.6px; margin-top: 6px; }
  .card--services .wordmark { left: 0; right: 0; top: 88px; }
  .card--contact .wordmark { left: 384px; width: 210px; top: 88px; }

  .swoosh { position: absolute; left: 0; top: 0; width: 622px; height: 357px; }

  .services {
    position: absolute;
    left: 27px;
    top: 208px;
    display: grid;
    grid-template-columns: 234px 178px auto;
    grid-auto-flow: column;
    grid-template-rows: repeat(5, 25.8px);
    list-style: none;
    color: #fff;
    font-size: 15.5px;
  }
  .services li { display: flex; align-items: center; gap: 5px; white-space: nowrap; }
  .tick { width: 16px; height: 16px; flex: none; }

  .person {
    position: absolute;
    left: 42px;
    top: 220px;
    font-family: "Montserrat", Arial, sans-serif;
  }
  .person__name { font-size: 22px; font-weight: 500; color: var(--ink); letter-spacing: 0.6px; }
  .person__title {
    position: absolute;
    left: 0; top: 247px; width: 622px; height: 20px;
  }
  .rule { position: absolute; top: 256px; height: 2px; background: var(--green-text); }
  .rule--left { left: 0; width: 38px; }
  .rule--right { left: 250px; right: 0; }
  .title-text {
    position: absolute; left: 42px; top: 246px;
    font-family: "Montserrat", Arial, sans-serif;
    font-size: 16px; font-weight: 500; color: var(--green-text); letter-spacing: 1px;
  }

  .contacts {
    position: absolute; top: 285px; left: 0; width: 622px; height: 22px;
    font-size: 15.5px; color: var(--ink);
  }
  .contacts span { position: absolute; display: flex; align-items: center; gap: 9px; white-space: nowrap; }
  .contacts svg { width: 14px; height: 14px; flex: none; }
  .contact--phone { left: 76px; }
  .contact--mobile { left: 220px; }
  .contact--email { left: 374px; }

  .web-band {
    position: absolute; left: 0; bottom: 0; width: 622px; height: 35px;
    background: var(--green-band);
    color: #fff; text-align: center;
    font-size: 15px; letter-spacing: 2.4px; line-height: 35px;
  }
</style>
</head>
<body>

<section class="card card--services" aria-label="Services side">
  <div class="wordmark">
    <span class="wordmark__name">KRAVEL</span>
    <span class="wordmark__sub">CONSTRUCTION LTD</span>
  </div>
  <svg class="swoosh" viewBox="0 0 622 357" aria-hidden="true">
    <path d="M0,145 Q311,175 622,145 V357 H0 Z" fill="var(--green-band)"/>
    <path d="M20,146 Q311,186 602,146 Q311,218 20,146 Z" fill="#fff"/>
    <path d="M35,152 Q311,196 595,152 Q311,252 35,152 Z" fill="var(--green-dark)"/>
  </svg>
  <ul class="services">
    <li><svg class="tick" viewBox="0 0 16 16"><circle cx="8" cy="8" r="6.8" fill="none" stroke="#fff" stroke-width="1.5"/><path d="M4.8 8.2l2.2 2.2 4.4-4.8" fill="none" stroke="#fff" stroke-width="1.7"/></svg>Kitchen Renovations</li>
    <li><svg class="tick" viewBox="0 0 16 16"><circle cx="8" cy="8" r="6.8" fill="none" stroke="#fff" stroke-width="1.5"/><path d="M4.8 8.2l2.2 2.2 4.4-4.8" fill="none" stroke="#fff" stroke-width="1.7"/></svg>Bathroom Renovations</li>
    <li><svg class="tick" viewBox="0 0 16 16"><circle cx="8" cy="8" r="6.8" fill="none" stroke="#fff" stroke-width="1.5"/><path d="M4.8 8.2l2.2 2.2 4.4-4.8" fill="none" stroke="#fff" stroke-width="1.7"/></svg>House Renovations</li>
    <li><svg class="tick" viewBox="0 0 16 16"><circle cx="8" cy="8" r="6.8" fill="none" stroke="#fff" stroke-width="1.5"/><path d="M4.8 8.2l2.2 2.2 4.4-4.8" fill="none" stroke="#fff" stroke-width="1.7"/></svg>Garage Conversions</li>
    <li><svg class="tick" viewBox="0 0 16 16"><circle cx="8" cy="8" r="6.8" fill="none" stroke="#fff" stroke-width="1.5"/><path d="M4.8 8.2l2.2 2.2 4.4-4.8" fill="none" stroke="#fff" stroke-width="1.7"/></svg>Extensions</li>
    <li><svg class="tick" viewBox="0 0 16 16"><circle cx="8" cy="8" r="6.8" fill="none" stroke="#fff" stroke-width="1.5"/><path d="M4.8 8.2l2.2 2.2 4.4-4.8" fill="none" stroke="#fff" stroke-width="1.7"/></svg>Loft Conversions</li>
    <li><svg class="tick" viewBox="0 0 16 16"><circle cx="8" cy="8" r="6.8" fill="none" stroke="#fff" stroke-width="1.5"/><path d="M4.8 8.2l2.2 2.2 4.4-4.8" fill="none" stroke="#fff" stroke-width="1.7"/></svg>Conservatories</li>
    <li><svg class="tick" viewBox="0 0 16 16"><circle cx="8" cy="8" r="6.8" fill="none" stroke="#fff" stroke-width="1.5"/><path d="M4.8 8.2l2.2 2.2 4.4-4.8" fill="none" stroke="#fff" stroke-width="1.7"/></svg>Carpentry</li>
    <li><svg class="tick" viewBox="0 0 16 16"><circle cx="8" cy="8" r="6.8" fill="none" stroke="#fff" stroke-width="1.5"/><path d="M4.8 8.2l2.2 2.2 4.4-4.8" fill="none" stroke="#fff" stroke-width="1.7"/></svg>Tiling</li>
    <li><svg class="tick" viewBox="0 0 16 16"><circle cx="8" cy="8" r="6.8" fill="none" stroke="#fff" stroke-width="1.5"/><path d="M4.8 8.2l2.2 2.2 4.4-4.8" fill="none" stroke="#fff" stroke-width="1.7"/></svg>Electrical</li>
    <li><svg class="tick" viewBox="0 0 16 16"><circle cx="8" cy="8" r="6.8" fill="none" stroke="#fff" stroke-width="1.5"/><path d="M4.8 8.2l2.2 2.2 4.4-4.8" fill="none" stroke="#fff" stroke-width="1.7"/></svg>Plumbing &amp; Heating</li>
    <li><svg class="tick" viewBox="0 0 16 16"><circle cx="8" cy="8" r="6.8" fill="none" stroke="#fff" stroke-width="1.5"/><path d="M4.8 8.2l2.2 2.2 4.4-4.8" fill="none" stroke="#fff" stroke-width="1.7"/></svg>Bricklaying</li>
    <li><svg class="tick" viewBox="0 0 16 16"><circle cx="8" cy="8" r="6.8" fill="none" stroke="#fff" stroke-width="1.5"/><path d="M4.8 8.2l2.2 2.2 4.4-4.8" fill="none" stroke="#fff" stroke-width="1.7"/></svg>Landscaping</li>
    <li><svg class="tick" viewBox="0 0 16 16"><circle cx="8" cy="8" r="6.8" fill="none" stroke="#fff" stroke-width="1.5"/><path d="M4.8 8.2l2.2 2.2 4.4-4.8" fill="none" stroke="#fff" stroke-width="1.7"/></svg>Decorating</li>
    <li><svg class="tick" viewBox="0 0 16 16"><circle cx="8" cy="8" r="6.8" fill="none" stroke="#fff" stroke-width="1.5"/><path d="M4.8 8.2l2.2 2.2 4.4-4.8" fill="none" stroke="#fff" stroke-width="1.7"/></svg>Plastering</li>
  </ul>
</section>

<section class="card card--contact" aria-label="Contact side">
  <div class="wordmark">
    <span class="wordmark__name">KRAVEL</span>
    <span class="wordmark__sub">CONSTRUCTION LTD</span>
  </div>
  <div class="person"><h1 class="person__name">TOMAS VERBELK</h1></div>
  <div class="rule rule--left"></div>
  <p class="title-text">MANAGING DIRECTOR</p>
  <div class="rule rule--right"></div>
  <div class="contacts">
    <span class="contact--phone"><svg viewBox="0 0 14 14"><path d="M3 1h2.5l1 3-1.6 1.2a7 7 0 0 0 3.9 3.9L10 7.5l3 1V11c0 1-1 2-2 2C5.5 12.5 1.5 8.5 1 3c0-1 1-2 2-2z" fill="var(--green)"/></svg>020 5194 6381</span>
    <span class="contact--mobile"><svg viewBox="0 0 14 14"><rect x="0.5" y="2.5" width="13" height="9" fill="var(--green)"/><path d="M0.5 2.5l6.5 5 6.5-5" fill="none" stroke="#fff" stroke-width="1.2"/></svg>07845319027</span>
    <span class="contact--email"><svg viewBox="0 0 14 14"><rect x="0.5" y="2.5" width="13" height="9" fill="var(--green)"/><path d="M0.5 2.5l6.5 5 6.5-5" fill="none" stroke="#fff" stroke-width="1.2"/></svg>tomas@kravel.co.uk</span>
  </div>
  <div class="web-band">WWW.KRAVEL.CO.UK</div>
</section>

</body>
</html>
```